Elm Ridge Baptist Church sign

We want a colourful, attractive sign that includes connection to being a Christian Church living in the foothills of the Canadian Rocky Mountains. As far as printed words, we need it to say “ Elm Ridge Baptist Church”. We are planning on a sign that is 6’ x 4’. Our church slogan is:
“ Live like Jesus, Love like Jesus”. This slogan could be included on the sign if space allows. To all designers; in talking with the communications team at our church, we want to eliminate the church’s slogan “ live like Jesus, live like Jesus “, from being on the sign.

```html
<!DOCTYPE html>
<html lang="en">
<head>
<meta charset="utf-8">
<title>Elm Ridge Baptist Church Sign</title>
<link rel="stylesheet" href="https://fonts.googleapis.com/css2?family=Crimson+Pro:wght@700&display=swap">
<style>
  :root {
    --backdrop: #7a7a7a;
    --sky-top: #5fa3dc;
    --sky-haze: #c9dcea;
    --mountain: #8fa6c0;
    --foothill: #4f6d3e;
    --forest: #2f4a2a;
    --gold-light: #e6e7a6;
    --gold: #b5b83a;
    --gold-dark: #8f9426;
    --white: #ffffff;
    --red-bright: #e21b24;
    --red: #b5181f;
    --red-deep: #8e1419;
  }
  * { margin: 0; padding: 0; box-sizing: border-box; }
  html, body {
    width: 889px; height: 1200px; overflow: hidden;
    background: var(--backdrop);
  }
  .sign {
    position: absolute; left: 20px; top: 317px;
    width: 849px; height: 566px;
    overflow: hidden;
    box-shadow: 4px 6px 14px rgba(0,0,0,0.35);
    font-family: "Crimson Pro", Georgia, serif;
  }
  .sign-art { position: absolute; inset: 0; width: 100%; height: 100%; display: block; }
  .church-name {
    position: absolute; left: 0; right: 0; top: 382px;
    text-align: center; color: var(--white);
    font-variant: small-caps; font-weight: 700;
    font-size: 110px; line-height: 72px;
    white-space: nowrap;
    text-shadow: 2px 2px 2px rgba(70,10,10,0.6);
  }
  .church-name span { display: block; }
</style>
</head>
<body>
  <div class="sign">
    <svg class="sign-art" viewBox="0 0 1307 870" preserveAspectRatio="none">
      <defs>
        <linearGradient id="landscapeTone" x1="0" y1="0" x2="0" y2="1">
          <stop offset="0" stop-color="var(--sky-top)"/>
          <stop offset="0.22" stop-color="var(--sky-haze)"/>
          <stop offset="0.32" stop-color="var(--mountain)"/>
          <stop offset="0.42" stop-color="var(--foothill)"/>
          <stop offset="0.7" stop-color="var(--forest)"/>
          <stop offset="1" stop-color="var(--foothill)"/>
        </linearGradient>
        <linearGradient id="goldBand" x1="0" y1="0" x2="1" y2="0">
          <stop offset="0" stop-color="var(--gold)"/>
          <stop offset="0.3" stop-color="var(--gold-light)"/>
          <stop offset="0.6" stop-color="var(--gold)"/>
          <stop offset="1" stop-color="var(--gold-dark)"/>
        </linearGradient>
        <radialGradient id="redField" cx="0.32" cy="0.65" r="0.75">
          <stop offset="0" stop-color="var(--red-bright)"/>
          <stop offset="0.6" stop-color="var(--red)"/>
          <stop offset="1" stop-color="var(--red-deep)"/>
        </radialGradient>
      </defs>
      <rect class="landscape" x="0" y="0" width="1307" height="620" fill="url(#landscapeTone)"
            role="img" aria-label="Photograph of the Rocky Mountains above forested foothills and a small town"/>
      <path class="arch" fill="var(--white)"
            d="M0,335 Q200,420 330,470 C430,370 880,370 985,470 Q1110,420 1307,335 L1307,370 Q655,720 0,370 Z"/>
      <path class="gold-band" fill="url(#goldBand)"
            d="M0,360 Q655,720 1307,360 L1307,455 Q655,665 0,455 Z"/>
      <path class="red-field" fill="url(#redField)"
            d="M0,455 Q655,665 1307,455 L1307,870 L0,870 Z"/>
      <path class="red-edge" fill="none" stroke="var(--red-deep)" stroke-width="5"
            d="M0,457 Q655,667 1307,457"/>
    </svg>
    <h1 class="church-name">
      <span>Elm Ridge</span>
      <span>Baptist Church</span>
    </h1>
  </div>
</body>
</html>
```